Law firm Seeks Modern and Engaging Site Redesign

Law firm seeks a new web site. Should be modern, but retaining existing logo. Needs to include contact section, professional bio, services offered, and contact information.

The site should be modern, responsive, and able to be SEO optimized.

The finished product should be coded in a Wordpress site, which I will provide. I can work with other platforms, including Wix, but WP is preferred.

Note the current site is https://www.tallowfieldlaw.example/#/home

Target Market(s)

Family Law Practice

Industry/Entity Type

Legal

Coding

Coded - Design and coding required

Number of Pages Required

4 page

Font styles to use
Sans Serif

Requirements
Must have
• Service description
Bio pages for partners
Contact Form
Awards/Publication page

```html
<!DOCTYPE html>
<html lang="en">
<head>
<meta charset="utf-8">
<title>Tallowfield Harrow, LLC — Attorneys at Law</title>
<link href="https://fonts.googleapis.com/css2?family=Lato:wght@400;700;900&family=Roboto:wght@300;400;500;700&display=swap" rel="stylesheet">
<style>
:root{
  --navy:#06316b;
  --navy-deep:#052a5c;
  --accent:#3b8fe2;
  --accent-strong:#1f7be0;
  --sky:#d7ecfa;
  --ink:#222;
  --muted:#555;
  --footer:#04060d;
  --send:#3cc56a;
  --white:#fff;
}
*{box-sizing:border-box;margin:0;padding:0}
html,body{width:1200px;height:3811px;overflow:hidden;background:var(--white)}
body{font-family:'Roboto',sans-serif;color:var(--ink);position:relative}
.page{position:relative;width:1200px;height:3811px;overflow:hidden}
.abs{position:absolute}

/* header */
.site-header{left:0;top:0;width:1200px;height:125px;background:linear-gradient(#fff,#f4f4f4)}
.brand{left:0;width:1200px;top:28px;text-align:center}
.brand-name{font-family:'Roboto',sans-serif;font-weight:300;font-size:28px;color:#4a4a4a;letter-spacing:.5px}
.brand-tag{font-size:10px;color:#3b6fb0;margin-top:1px}
.main-nav{left:0;width:1200px;top:90px;text-align:center;font-size:16px;color:#2d5da8}
.main-nav span{margin:0 8px}

/* hero */
.hero{left:0;top:125px;width:1200px;height:365px;background:linear-gradient(90deg,#3a2418,#6a4330 30%,#4a2e20 60%,#2c1a12);}

/* intro */
.intro{left:0;top:430px;width:1200px;height:628px}
.portrait{background:linear-gradient(#cfd5df,#263a5e 55%,#1d2b45)}
.portrait-left{left:80px;top:150px;width:240px;height:478px;border-radius:110px 110px 0 0}
.portrait-right{left:865px;top:190px;width:255px;height:438px;border-radius:110px 110px 0 0}
.intro-text{left:350px;top:162px;width:500px;font-size:12.6px;line-height:20px;color:#333;text-align:center}
.intro-text p{margin-bottom:12px}

/* cta */
.cta-text{left:88px;top:1084px;font-family:'Lato',sans-serif;font-weight:700;font-size:27px;line-height:34px;color:#4ea0ec}
.cta-text strong{color:#fff}
.cta-btn{left:936px;top:1103px;width:175px;height:56px;border-radius:28px;background:var(--accent-strong);color:#fff;font-weight:700;font-size:13px;display:flex;align-items:center;justify-content:center;gap:10px}

/* section titles */
.section-title{left:0;width:1200px;text-align:center;font-family:'Lato',sans-serif;font-weight:700;font-size:32px;color:#222;letter-spacing:-.5px}
.section-title em{font-style:normal;color:var(--accent)}
.section-sub{left:0;width:1200px;text-align:center;font-size:14.5px;line-height:23px;color:#555}
.divider{left:573px;width:54px;height:4px}

/* attorneys */
.card{top:1390px;width:252px;height:502px;background:#fff;box-shadow:0 2px 8px rgba(0,0,0,.12);padding:9px}
.card-photo{width:234px;height:350px;background:linear-gradient(#b7a58e,#2a3550 60%,#4b3a2c)}
.card-photo.alt{background:linear-gradient(#f4f4f4,#c8a48c 40%,#1f4fb5 80%)}
.card-name{font-family:'Roboto',sans-serif;font-weight:500;font-size:20px;text-align:center;margin-top:16px;color:#111;letter-spacing:-.5px}
.badge{width:164px;height:74px;margin:14px auto 0;border-radius:6px;background:#fff;border:3px solid #f28a1a;box-shadow:0 2px 4px rgba(0,0,0,.2);position:relative;overflow:hidden}
.badge::after{content:"";position:absolute;left:0;right:0;bottom:0;height:22px;background:#f28a1a}

/* services */
.col-title{font-family:'Lato',sans-serif;font-weight:700;font-size:31px;color:#222;letter-spacing:-.5px}
.col-title em{font-style:normal;color:var(--accent)}
.col-lead{font-size:16px;color:#333}
.acc{list-style:none}
.acc li{font-size:12.5px;color:#2d6fc4;font-weight:500;height:44px;display:flex;align-items:flex-start;gap:14px}
.acc li svg{flex:none;margin-top:1px}
.acc li.open{height:auto;flex-direction:column;gap:8px}
.acc .head{display:flex;gap:14px}
.acc .body{font-size:12px;line-height:17px;color:#666;font-weight:400;padding-left:27px;margin-bottom:14px;width:460px}

/* contact */
.contact-title{left:0;width:1200px;text-align:center;top:2950px;font-family:'Lato',sans-serif;font-weight:700;font-size:32px;color:var(--accent)}
.contact-sub{left:0;width:1200px;text-align:center;top:2993px;font-size:15px;color:#fff}
.map{left:89px;top:3041px;width:666px;height:487px;background:linear-gradient(135deg,#e9ecd6,#dfe6ee 50%,#a9cbe9)}
.form{left:773px;top:3041px;width:337px;height:487px;background:#fff;border-radius:22px;padding:18px 18px}
.form label{display:block;font-size:14px;color:#666;margin-bottom:3px}
.field{height:30px;border:1px solid #bbb;font-size:11px;color:#999;padding:8px 10px;margin-bottom:11px}
.field.select{font-size:15px;color:#444;padding:5px 10px;display:flex;justify-content:space-between;align-items:center}
.field.area{height:108px}
.send{height:34px;background:var(--send);color:#fff;font-weight:700;font-size:12px;display:flex;align-items:center;justify-content:center;margin-top:-3px}

/* footer */
.footer-brand{left:0;width:1200px;top:3670px;text-align:center}
.footer-brand .brand-name{color:#8a8a8a}
.footer-info{left:0;width:1200px;top:3748px;text-align:center;font-size:12.5px;line-height:20px;color:#fff;font-weight:500}
</style>
</head>
<body>
<div class="page">

  <header class="abs site-header">
    <div class="abs brand">
      <div class="brand-name">Tallowfield Harrow</div>
      <div class="brand-tag">Attorneys at Law</div>
    </div>
    <nav class="abs main-nav"><span>HOME</span>|<span>SERVICES</span>|<span>ABOUT US</span>|<span>CONTACT US</span></nav>
  </header>

  <div class="abs hero" role="img" aria-label="Row of leather-bound law books with brass scales of justice"></div>

  <!-- section backgrounds -->
  <svg class="abs" style="left:0;top:0" width="1200" height="3811" aria-hidden="true">
    <defs>
      <linearGradient id="introBg" x1="0" y1="0" x2="0" y2="1">
        <stop offset="0" stop-color="#ffffff"/><stop offset="1" stop-color="#cfcfcf"/>
      </linearGradient>
    </defs>
    <polygon points="0,490 600,432 1200,490 1200,1058 0,1058" fill="url(#introBg)"/>
    <polygon points="0,1058 1200,1058 1200,1273 600,1206 0,1273" fill="#06316b"/>
    <polygon points="0,1273 600,1206 1200,1273 1200,2010 600,1948 0,2010" fill="#d7ecfa"/>
    <polygon points="0,2883 600,2820 1200,2883 1200,3600 600,3583 0,3600" fill="#06316b"/>
    <polygon points="0,3600 600,3583 1200,3600 1200,3811 0,3811" fill="#04060d"/>
  </svg>

  <section class="abs intro">
    <div class="abs portrait portrait-left" role="img" aria-label="Portrait of partner Daniel R. Tallowfield in a navy suit"></div>
    <div class="abs portrait portrait-right" role="img" aria-label="Portrait of partner Marcus J. Harrow in a navy suit"></div>
    <div class="abs intro-text">
      <p>The law firm of Tallowfield Harrow, LLC is based in Bergen County, conveniently located in Fairlow, New Jersey in 14 Meridian Plaza. We serve the needs of clients throughout Bergen County, as well as, clients from several other counties, including, but not limited to, Passaic, Morris, Essex and Hudson. Between our partners, we have over 30+ years of experience assisting clients with all of their family law and criminal law needs.</p>
      <p>Often times the areas of family law and criminal law cross paths, which can be both emotionally and financially complex. We understand that our client's case is unique and pride ourselves on being responsive to all of our clients needs.</p>
      <p>Mr. Tallowfield began his career as the law clerk to the Honorable Thomas A. Wexley, J.S.C., retired, the then Presiding Judge of the Criminal Part and thereafter as an Assistant Prosecutor with the Bergen County Prosecutors Office. Mr. Harrow began his career as the law clerk to the Honorable Edwin P. Carrow, J.S.C., retired, who oversaw the Court's Juvenile Delinquency docket, DYFS (now DCP&amp;P) docket and all other Family Part matters. As a result of their experience in the court system, Mr. Tallowfield and Mr. Harrow bring a unique perspective to their practice.</p>
      <p>Both Mr. Tallowfield and Mr. Harrow practiced privately for well over a decade as partners in two of Bergen County's most established Family Law firms before joining together to use their knowledge and experience to assist their clients with all of their legal needs.</p>
    </div>
  </section>

  <div class="abs cta-text">Whether your needs are family or criminal law related,<br>contact <strong>Tallowfield Harrow, LLC</strong> to schedule a consultation.</div>
  <div class="abs cta-btn">CONTACT US
    <svg width="14" height="10" viewBox="0 0 14 10"><path d="M0 5h12M8 1l4 4-4 4" stroke="#fff" stroke-width="1.5" fill="none"/></svg>
  </div>

  <!-- attorneys -->
  <h2 class="abs section-title" style="top:1250px">Our <em>Attorney</em></h2>
  <p class="abs section-sub" style="top:1303px">Our legal team brings more than 30+ years of experience to assist in all of your family law needs.</p>
  <svg class="abs divider" style="top:1336px" viewBox="0 0 54 4"><circle cx="2" cy="2" r="1.5" fill="#3b8fe2"/><circle cx="8" cy="2" r="1.5" fill="#3b8fe2"/><circle cx="14" cy="2" r="1.5" fill="#3b8fe2"/><rect x="20" y="0.5" width="34" height="3" fill="#3b8fe2"/></svg>

  <div class="abs card" style="left:84px">
    <div class="card-photo" role="img" aria-label="Photo of Daniel R. Tallowfield seated at a desk"></div>
    <div class="card-name">Daniel R. Tallowfield</div>
    <div class="badge" role="img" aria-label="Peer rating badge"></div>
  </div>
  <div class="abs card" style="left:344px">
    <div class="card-photo" role="img" aria-label="Photo of Marcus J. Harrow seated at a desk"></div>
    <div class="card-name">Marcus J. Harrow</div>
    <div class="badge" role="img" aria-label="Peer rating badge"></div>
  </div>
  <div class="abs card" style="left:605px">
    <div class="card-photo" role="img" aria-label="Photo of an attorney seated in an office"></div>
    <div class="card-name">Daniel R. Tallowfield</div>
    <div class="badge" role="img" aria-label="Peer rating badge"></div>
  </div>
  <div class="abs card" style="left:865px">
    <div class="card-photo alt" role="img" aria-label="Portrait of Sofia E. Renaldi"></div>
    <div class="card-name">Sofia E. Renaldi</div>
    <div class="badge" role="img" aria-label="Peer rating badge"></div>
  </div>

  <!-- services -->
  <h2 class="abs section-title" style="top:2044px">Our <em>Services</em></h2>
  <p class="abs section-sub" style="top:2097px">Often times the areas of family law and criminal law cross paths, which can be both emotionally and financially complex.<br>We understand that our client's case is unique and pride ourselves on being responsive to all of our clients needs.<br>Our services cover all kind of family and criminal law matters.</p>
  <svg class="abs divider" style="top:2174px" viewBox="0 0 54 4"><circle cx="2" cy="2" r="1.5" fill="#3b8fe2"/><circle cx="8" cy="2" r="1.5" fill="#3b8fe2"/><circle cx="14" cy="2" r="1.5" fill="#3b8fe2"/><rect x="20" y="0.5" width="34" height="3" fill="#3b8fe2"/></svg>

  <div class="abs" style="left:125px;top:2232px;width:480px">
    <h3 class="col-title">Family <em>Law</em></h3>
    <p class="col-lead" style="margin-top:20px">Our firm accepts all kinds of family law matters, including:</p>
    <ul class="acc" style="margin-top:34px;margin-left:-9px">
      <li class="open"><div class="head"><svg width="13" height="13" viewBox="0 0 13 13"><path d="M2 6l4.5-4 4.5 4M2 11l4.5-4 4.5 4" stroke="#2d6fc4" stroke-width="1.8" fill="none"/></svg>Divorce</div><div class="body">Lorem ipsum dolor sit amet, consectetur adipiscing elit. Ut elit tellus, luctus nec ullamcorper mattis, pulvinar dapibus leo.</div></li>
      <li><svg width="13" height="13" viewBox="0 0 13 13"><path d="M1.5 4l5 5 5-5" stroke="#2d6fc4" stroke-width="2" fill="none"/></svg>Child Custody</li>
      <li><svg width="13" height="13" viewBox="0 0 13 13"><path d="M1.5 4l5 5 5-5" stroke="#2d6fc4" stroke-width="2" fill="none"/></svg>Child Support</li>
      <li><svg width="13" height="13" viewBox="0 0 13 13"><path d="M1.5 4l5 5 5-5" stroke="#2d6fc4" stroke-width="2" fill="none"/></svg>Alimony</li>
      <li><svg width="13" height="13" viewBox="0 0 13 13"><path d="M1.5 4l5 5 5-5" stroke="#2d6fc4" stroke-width="2" fill="none"/></svg>Division of Assets and Liabilities</li>
      <li><svg width="13" height="13" viewBox="0 0 13 13"><path d="M1.5 4l5 5 5-5" stroke="#2d6fc4" stroke-width="2" fill="none"/></svg>Pre-nuptial agreements</li>
      <li><svg width="13" height="13" viewBox="0 0 13 13"><path d="M1.5 4l5 5 5-5" stroke="#2d6fc4" stroke-width="2" fill="none"/></svg>High-net worth and complex divorce cases</li>
      <li><svg width="13" height="13" viewBox="0 0 13 13"><path d="M1.5 4l5 5 5-5" stroke="#2d6fc4" stroke-width="2" fill="none"/></svg>Domestic violence</li>
      <li><svg width="13" height="13" viewBox="0 0 13 13"><path d="M1.5 4l5 5 5-5" stroke="#2d6fc4" stroke-width="2" fill="none"/></svg>DCP&amp;P (formerly DYFS)</li>
      <li><svg width="13" height="13" viewBox="0 0 13 13"><path d="M1.5 4l5 5 5-5" stroke="#2d6fc4" stroke-width="2" fill="none"/></svg>Support Modification</li>
    </ul>
  </div>

  <div class="abs" style="left:645px;top:2232px;width:480px">
    <h3 class="col-title">Criminal <em>Law</em></h3>
    <p class="col-lead" style="margin-top:20px">Our firm accepts all kinds of family law matters, including:</p>
    <ul class="acc" style="margin-top:34px;margin-left:-9px">
      <li class="open"><div class="head"><svg width="13" height="13" viewBox="0 0 13 13"><path d="M2 6l4.5-4 4.5 4M2 11l4.5-4 4.5 4" stroke="#2d6fc4" stroke-width="1.8" fill="none"/></svg>Assault</div><div class="body">Lorem ipsum dolor sit amet, consectetur adipiscing elit. Ut elit tellus, luctus nec ullamcorper mattis, pulvinar dapibus leo.</div></li>
      <li><svg width="13" height="13" viewBox="0 0 13 13"><path d="M1.5 4l5 5 5-5" stroke="#2d6fc4" stroke-width="2" fill="none"/></svg>Domestic Violence</li>
      <li><svg width="13" height="13" viewBox="0 0 13 13"><path d="M1.5 4l5 5 5-5" stroke="#2d6fc4" stroke-width="2" fill="none"/></svg>Drug Crimes</li>
      <li><svg width="13" height="13" viewBox="0 0 13 13"><path d="M1.5 4l5 5 5-5" stroke="#2d6fc4" stroke-width="2" fill="none"/></svg>DWI/DUI</li>
      <li><svg width="13" height="13" viewBox="0 0 13 13"><path d="M1.5 4l5 5 5-5" stroke="#2d6fc4" stroke-width="2" fill="none"/></svg>Sex Crimes</li>
      <li><svg width="13" height="13" viewBox="0 0 13 13"><path d="M1.5 4l5 5 5-5" stroke="#2d6fc4" stroke-width="2" fill="none"/></svg>Theft/Fraud Crimes</li>
      <li><svg width="13" height="13" viewBox="0 0 13 13"><path d="M1.5 4l5 5 5-5" stroke="#2d6fc4" stroke-width="2" fill="none"/></svg>Expungements</li>
    </ul>
  </div>

  <!-- contact -->
  <h2 class="abs contact-title">Contact Us</h2>
  <p class="abs contact-sub">Whether your needs are family or criminal law related, contact Tallowfield Harrow, LLC to schedule a consultation.</p>
  <svg class="abs divider" style="top:3017px" viewBox="0 0 54 4"><circle cx="2" cy="2" r="1.5" fill="#3b8fe2"/><circle cx="8" cy="2" r="1.5" fill="#3b8fe2"/><circle cx="14" cy="2" r="1.5" fill="#3b8fe2"/><rect x="20" y="0.5" width="34" height="3" fill="#3b8fe2"/></svg>

  <div class="abs map" role="img" aria-label="Street map showing the office location in northern New Jersey"></div>

  <form class="abs form">
    <label>Name</label><div class="field">Name</div>
    <label>Last Name</label><div class="field">Last Name</div>
    <label>Email</label><div class="field">Email</div>
    <label>Phone</label><div class="field">Phone</div>
    <label>Practise Area</label><div class="field select">Please Choose <svg width="8" height="5" viewBox="0 0 8 5"><path d="M0 0h8L4 5z" fill="#444"/></svg></div>
    <label>Message</label><div class="field area">Message</div>
    <div class="send">SEND</div>
  </form>

  <!-- footer -->
  <footer>
    <div class="abs footer-brand">
      <div class="brand-name">Tallowfield Harrow</div>
      <div class="brand-tag">Attorneys at Law</div>
    </div>
    <div class="abs footer-info">Tallowfield &amp; Harrow LLC – 14 Meridian Plaza Drive Suite 210 Fairlow, NJ 07000<br>Phone: (201) 555-0142 Fax: (201) 555-0178</div>
  </footer>

</div>
</body>
</html>
```